Brightwave Reach - Business Card

We need a business card for a Social Media Marketing company that specializes in online marketing for small businesses in Canada using common Social Media platforms such as Pictora, Kinloop, Flickwisp & Chirpo.

I have uploaded a copy of our logo which I would like utilized in the business card. We would like the business card to be modern yet classy design.

Our website is www.brightwavereach.ca

Industry/Entity Type

Marketing

Contact Information for Business Card

Email: info@brightwavereach.ca
Website: www.brightwavereach.ca
Telephone: 604-392-5108

Colors

Designer to choose colors to be used in the design.

Requirements
Must have
• Social Media icons on reverse
• Please add some designs with color.

```html
<!DOCTYPE html>
<html lang="en">
<head>
<meta charset="UTF-8">
<title>Brightwave Reach – Business Card</title>
<link href="https://fonts.googleapis.com/css2?family=Lato:wght@400;700&display=swap" rel="stylesheet">
<style>
  :root {
    --page-bg: #4a4a4a;
    --card-dark: #232323;
    --card-light: #3d3d3d;
    --accent: #e0762c;
    --text-light: #f4f4f4;
    --text-soft: #d9d9d9;
  }
  * { box-sizing: border-box; margin: 0; padding: 0; }
  html, body { width: 1200px; height: 800px; overflow: hidden; }
  body {
    background: var(--page-bg);
    font-family: "Lato", sans-serif;
    display: flex;
    align-items: center;
    justify-content: center;
    gap: 40px;
  }
  .card {
    width: 540px;
    height: 309px;
    border-radius: 4px;
    background: radial-gradient(ellipse at 40% 45%, var(--card-light) 0%, var(--card-dark) 75%);
    box-shadow: 0 10px 30px rgba(0,0,0,0.45);
    position: relative;
    color: var(--text-light);
    overflow: hidden;
  }

  /* Wordmark */
  .wordmark {
    display: flex;
    align-items: center;
    gap: 12px;
    font-weight: 700;
    color: var(--text-light);
    text-transform: uppercase;
    letter-spacing: 1px;
    white-space: nowrap;
  }
  .wordmark-square {
    width: 22px;
    height: 22px;
    border: 3px solid var(--text-light);
    flex-shrink: 0;
  }
  .wordmark-lines { display: flex; flex-direction: column; line-height: 1.1; }

  /* Front face */
  .card-front { display: flex; align-items: center; }
  .card-front .brand-side {
    width: 270px;
    padding: 0 20px;
    display: flex;
    justify-content: center;
  }
  .card-front .wordmark { font-size: 24px; }
  .divider {
    width: 2px;
    height: 130px;
    background: var(--accent);
    flex-shrink: 0;
  }
  .contact-side { padding-left: 32px; }
  .person-name {
    color: var(--accent);
    font-size: 24px;
    font-weight: 700;
    line-height: 1.1;
  }
  .person-role {
    font-size: 15px;
    color: var(--text-soft);
    margin-bottom: 18px;
  }
  .contact-list { list-style: none; }
  .contact-item {
    display: flex;
    align-items: center;
    gap: 12px;
    font-size: 16px;
    line-height: 1.5;
    white-space: nowrap;
  }
  .contact-icon { width: 14px; height: 14px; fill: var(--accent); flex-shrink: 0; }

  /* Back face */
  .card-back {
    display: flex;
    flex-direction: column;
    align-items: center;
    justify-content: center;
    gap: 60px;
  }
  .card-back .wordmark { font-size: 28px; }
  .social-row {
    display: flex;
    gap: 34px;
    list-style: none;
  }
  .social-item {
    display: flex;
    align-items: center;
    gap: 8px;
    font-size: 14px;
    font-weight: 700;
    color: var(--text-light);
  }
  .social-square {
    width: 16px;
    height: 16px;
    border-radius: 3px;
    background: var(--accent);
  }
</style>
</head>
<body>

  <section class="card card-front" aria-label="Business card front">
    <div class="brand-side">
      <div class="wordmark">
        <span class="wordmark-square"></span>
        <span class="wordmark-lines"><span>Brightwave</span><span>Reach</span></span>
      </div>
    </div>
    <div class="divider"></div>
    <div class="contact-side">
      <p class="person-name">Daniel Mercer</p>
      <p class="person-role">Manager</p>
      <ul class="contact-list">
        <li class="contact-item">
          <svg class="contact-icon" viewBox="0 0 24 24" aria-hidden="true"><path d="M6.6 10.8c1.4 2.8 3.8 5.1 6.6 6.6l2.2-2.2c.3-.3.7-.4 1-.2 1.1.4 2.3.6 3.6.6.6 0 1 .4 1 1V20c0 .6-.4 1-1 1C10.6 21 3 13.4 3 4c0-.6.4-1 1-1h3.5c.6 0 1 .4 1 1 0 1.3.2 2.5.6 3.6.1.3 0 .7-.2 1L6.6 10.8z"/></svg>
          604-392-5108
        </li>
        <li class="contact-item">
          <svg class="contact-icon" viewBox="0 0 24 24" aria-hidden="true"><path d="M2 5h20v2l-10 6L2 7zM2 9l10 6 10-6v10H2z"/></svg>
          info@brightwavereach.ca
        </li>
        <li class="contact-item">
          <svg class="contact-icon" viewBox="0 0 24 24" aria-hidden="true"><path d="M12 2a10 10 0 1 0 0 20 10 10 0 0 0 0-20zm6.9 6h-3a15 15 0 0 0-1.3-3.9A8 8 0 0 1 18.9 8zM12 4c.8 1.2 1.5 2.5 1.9 4h-3.8c.4-1.5 1.1-2.8 1.9-4zM4.3 14a8 8 0 0 1 0-4h3.4a16 16 0 0 0 0 4zm.8 2h3a15 15 0 0 0 1.3 3.9A8 8 0 0 1 5.1 16zm3-8h-3a8 8 0 0 1 4.3-3.9A15 15 0 0 0 8.1 8zM12 20c-.8-1.2-1.5-2.5-1.9-4h3.8c-.4 1.5-1.1 2.8-1.9 4zm2.3-6H9.7a14 14 0 0 1 0-4h4.6a14 14 0 0 1 0 4zm.3 5.9a15 15 0 0 0 1.3-3.9h3a8 8 0 0 1-4.3 3.9zm1.7-5.9a16 16 0 0 0 0-4h3.4a8 8 0 0 1 0 4z"/></svg>
          www.brightwavereach.ca
        </li>
      </ul>
    </div>
  </section>

  <section class="card card-back" aria-label="Business card back">
    <div class="wordmark"><span class="wordmark-square"></span>Brightwave Reach</div>
    <ul class="social-row">
      <li class="social-item"><span class="social-square"></span>Kinloop</li>
      <li class="social-item"><span class="social-square"></span>Pictora</li>
      <li class="social-item"><span class="social-square"></span>Chirpo</li>
      <li class="social-item"><span class="social-square"></span>Flickwisp</li>
    </ul>
  </section>

</body>
</html>
```